Pelmora needs stationery design

We need desings for presentation cards and letter head for our company. It would be better that the letterhead uses our logo with white background and the presentation card the logo with the black background for the back of the card and the text (name, phone
Updates

Necesitas un par de días antes de escoger al ganador

Colors
0455a3
ec1f27
000000

Requirements
Must have
• Use company logo and colors

```html
<!DOCTYPE html>
<html lang="en">
<head>
<meta charset="utf-8">
<title>Pelmora Stationery</title>
<link href="https://fonts.googleapis.com/css2?family=PT+Sans:wght@400;700&display=swap" rel="stylesheet">
<style>
  :root {
    --backdrop: #dcdddf;
    --paper: #ffffff;
    --ink: #000000;
    --text: #1d1d1f;
    --brand-blue: #0455a3;
    --brand-red: #ec1f27;
  }
  * { margin: 0; padding: 0; box-sizing: border-box; }
  html, body { width: 1200px; height: 1123px; overflow: hidden; }
  body {
    position: relative;
    background: var(--backdrop);
    font-family: "PT Sans", sans-serif;
    color: var(--text);
  }
  .letterhead, .card { position: absolute; box-shadow: 0 1px 4px rgba(0,0,0,0.12); }
  .letterhead { left: 83px; top: 83px; width: 676px; height: 956px; background: var(--paper); }
  .wordmark {
    position: absolute; left: 0; right: 0; text-align: center;
    font-weight: 400; line-height: 1; color: var(--ink);
  }
  .letterhead .wordmark { top: 44px; font-size: 44px; letter-spacing: 8px; padding-left: 8px; }
  .footer-info {
    position: absolute; left: 33px; top: 921px; width: 568px;
    display: flex; justify-content: space-between; align-items: center;
    font-size: 9px; white-space: nowrap;
    padding-bottom: 6px; border-bottom: 1px solid var(--ink);
  }
  .footer-info strong { font-weight: 700; }
  .contact { display: inline-flex; align-items: center; gap: 3px; }
  .contact svg { width: 8px; height: 8px; fill: var(--ink); }
  .brand-square { position: absolute; background: var(--brand-blue); }
  .letterhead .brand-square { left: 612px; top: 907px; width: 31px; height: 32px; }

  .card { left: 842px; width: 274px; height: 153px; }
  .card-back { top: 396px; background: var(--ink); }
  .card-back .wordmark { top: 62px; font-size: 28px; color: var(--paper); letter-spacing: 7px; padding-left: 7px; }
  .card-url {
    position: absolute; left: 0; right: 0; top: 134px; text-align: center;
    font-size: 7.5px; font-weight: 700; color: var(--paper);
  }
  .card-front { top: 574px; background: var(--paper); }
  .holder-name { position: absolute; left: 0; right: 0; top: 61px; text-align: center; font-size: 10.5px; font-weight: 700; }
  .holder-title { position: absolute; left: 0; right: 0; top: 75px; text-align: center; font-size: 7.5px; }
  .card-contacts {
    position: absolute; left: 17px; top: 127px; width: 215px;
    display: flex; gap: 10px; font-size: 7.5px; white-space: nowrap;
    padding-bottom: 4px; border-bottom: 1px solid var(--ink);
  }
  .card-contacts .contact svg { width: 7px; height: 7px; }
  .card-front .brand-square { left: 237px; top: 119px; width: 21px; height: 22px; }
</style>
</head>
<body>
  <section class="letterhead">
    <div class="wordmark">PELMORA</div>
    <div class="footer-info">
      <span><strong>PELMORA SA</strong> Calle Ombú Norte 1234, C1427BDE CABA</span>
      <span class="contact"><svg viewBox="0 0 10 10"><path d="M2 0.5 L3.6 0.5 L4.2 3 L3 3.8 C3.6 5.2 4.8 6.4 6.2 7 L7 5.8 L9.5 6.4 L9.5 8 C9.5 9 8.8 9.5 8 9.5 C4 9.3 0.7 6 0.5 2 C0.5 1.2 1 0.5 2 0.5Z"/></svg>11 4820-5316</span>
      <span class="contact"><svg viewBox="0 0 10 8"><path d="M0 0 H10 V8 H0Z M1 1 L5 4.5 L9 1Z" fill-rule="evenodd"/></svg>info@pelmora.com</span>
      <span class="contact"><svg viewBox="0 0 10 10" fill="none" stroke="#000" stroke-width="0.8" style="fill:none"><circle cx="5" cy="5" r="4.4"/><ellipse cx="5" cy="5" rx="2" ry="4.4"/><path d="M0.6 5 H9.4 M1.5 2.7 H8.5 M1.5 7.3 H8.5"/></svg>www.pelmora.com</span>
    </div>
    <div class="brand-square"></div>
  </section>

  <section class="card card-back">
    <div class="wordmark">PELMORA</div>
    <div class="card-url">www.PELMORA.com</div>
  </section>

  <section class="card card-front">
    <div class="holder-name">YOUR NAME</div>
    <div class="holder-title">Title</div>
    <div class="card-contacts">
      <span class="contact"><svg viewBox="0 0 10 10"><path d="M2 0.5 L3.6 0.5 L4.2 3 L3 3.8 C3.6 5.2 4.8 6.4 6.2 7 L7 5.8 L9.5 6.4 L9.5 8 C9.5 9 8.8 9.5 8 9.5 C4 9.3 0.7 6 0.5 2 C0.5 1.2 1 0.5 2 0.5Z"/></svg>11 4820-5316</span>
      <span class="contact"><svg viewBox="0 0 10 8"><path d="M0 0 H10 V8 H0Z M1 1 L5 4.5 L9 1Z" fill-rule="evenodd"/></svg>yourname@pelmora.com</span>
    </div>
    <div class="brand-square"></div>
  </section>
</body>
</html>
```